Design a premium label for the most expensive honey in the world: Manuka honey.

Manuka honey is originaire from New Zealand and recognized for its natural antibacterial activity. Rare and expensive, it is used in hospital as medical grade mainly to cure burns and wounds... Household will use it out of a pot like a "supplement" or to cure all sorts of ailments.
The label must feel:
- Premium and elegant .
- Reflect strongly its origin New Zealand. Use maori design but be careful of copyright. Must be styled.
- Purity and trust it is the real deal. Feel strongly that it is not an ersatz...
- Health and "medical" use.
Label must have:
* Brand: TOROWAI DOWNS
* MANUKA HONEY
* Made in New Zealand
* e250g
* MGO300
Target Market(s)
Export.

```html
<!DOCTYPE html>
<html lang="en">
<head>
<meta charset="utf-8">
<title>Torowai Downs Manuka Honey – Label Presentation</title>
<link rel="stylesheet" href="https://fonts.googleapis.com/css2?family=Newsreader:opsz,wght@6..72,400;6..72,500&family=Lato:wght@700&display=swap">
<style>
  :root {
    --page-white: #ffffff;
    --board-black: #000000;
    --label-grey: #1e1e1e;
    --gold: #c9a24a;
    --gold-deep: #c49a3c;
    --text-white: #ffffff;
    --serif: "Newsreader", "Times New Roman", serif;
    --sans: "Lato", "Helvetica Neue", Arial, sans-serif;
  }
  * { margin: 0; padding: 0; box-sizing: border-box; }
  html, body { width: 1200px; height: 1200px; overflow: hidden; background: var(--page-white); }
  .board { position: relative; width: 1200px; height: 1200px; background: var(--page-white); }

  /* Label artwork */
  .label {
    position: absolute; left: 371px; top: 87px; width: 457px; height: 456px;
    background: var(--label-grey); border-radius: 38px; color: var(--gold);
    font-family: var(--serif); text-align: center;
  }
  .label__brand {
    position: absolute; left: 0; right: 0; top: 140px;
    font-size: 26px; font-weight: 400; line-height: 1;
  }
  .label__product {
    position: absolute; left: 0; right: 0; top: 200px;
    font-size: 54px; font-weight: 500; line-height: 1; letter-spacing: -0.5px;
  }
  .label__rule {
    position: absolute; left: 98px; width: 262px; top: 266px; height: 3px; background: var(--gold);
  }
  .label__origin {
    position: absolute; left: 0; right: 0; top: 282px;
    font-size: 31px; line-height: 1;
  }
  .label__grade {
    position: absolute; left: 166px; top: 343px; width: 126px; height: 40px;
    background: var(--gold); color: var(--label-grey);
    font-size: 25px; line-height: 40px;
  }
  .label__weight {
    position: absolute; left: 0; right: 0; top: 408px;
    font-size: 30px; line-height: 1;
  }

  /* Rationale panel */
  .rationale {
    position: absolute; left: 0; top: 600px; width: 1200px; height: 600px;
    background: var(--board-black); color: var(--text-white); font-family: var(--sans);
  }
  .jar-photo {
    position: absolute; left: 67px; top: 73px; width: 463px; height: 462px;
    background: linear-gradient(180deg, #2e3440 0%, #262b35 55%, #d9c08e 58%, #e8d3a4 100%);
  }
  .rationale__title {
    position: absolute; left: 581px; top: 70px; width: 540px;
    font-size: 25px; font-weight: 700; letter-spacing: 0.5px; line-height: 1; white-space: nowrap;
  }
  .swatch { position: absolute; width: 86px; height: 86px; }
  .swatch--flower { left: 663px; top: 133px; background: #eab0b6; }
  .swatch--pattern { left: 663px; top: 274px; background: #7a2a24; }
  .swatch--grey { left: 663px; top: 413px; background: var(--label-grey); }
  .swatch--gold { left: 922px; top: 413px; background: linear-gradient(180deg, #c9a24a, #c6983a); }
  .caption {
    position: absolute; width: 280px; text-align: center;
    font-size: 16px; font-weight: 700; letter-spacing: 0.3px; line-height: 20px;
  }
  .caption--flower { left: 566px; top: 230px; }
  .caption--pattern { left: 566px; top: 371px; }
  .caption--grey { left: 566px; top: 509px; }
  .caption--gold { left: 825px; top: 509px; }
  .brand-mark {
    position: absolute; left: 851px; top: 220px; width: 230px; text-align: center;
    font-family: var(--serif); font-size: 34px; color: var(--gold); line-height: 1;
  }
</style>
</head>
<body>
<div class="board">
  <section class="label">
    <p class="label__brand">torowai downs</p>
    <h1 class="label__product">MANUKA HONEY</h1>
    <div class="label__rule"></div>
    <p class="label__origin">Made in New Zealand</p>
    <p class="label__grade">MGO300</p>
    <p class="label__weight">E250g</p>
  </section>

  <section class="rationale">
    <div class="jar-photo" role="img" aria-label="Photo of the dark amber honey jar wearing the label, on a light wood surface against a dark grey backdrop"></div>
    <h2 class="rationale__title">RATIONALE FOR LOGO MARK AND LABEL</h2>

    <div class="swatch swatch--flower" role="img" aria-label="Pink manuka flower illustration"></div>
    <p class="caption caption--flower">MANUKA FLOWER</p>

    <div class="swatch swatch--pattern" role="img" aria-label="Maori koru pattern in cream and deep red"></div>
    <p class="caption caption--pattern">MAORI PATTERN</p>

    <div class="swatch swatch--grey"></div>
    <p class="caption caption--grey">MATT VERY DARK GREY LABEL<br>IS SOPHISTCATED</p>

    <div class="swatch swatch--gold"></div>
    <p class="caption caption--gold">GOLD IS LUXURY</p>

    <p class="brand-mark">torowai downs</p>
  </section>
</div>
</body>
</html>
```